Dance School poster for end of year dance concert for mainly young girls.

We need an A3 portrait poster for our end of year concert.
Designs are attached of posters from previous 2 years as a reference only.
The theme of our concert this year is "Let's Dance" which we want to convey a general feel of energy & fun with dance.
Dance styles in the concert include Jazz & Hip Hop.
Bright colors are preferred in the design.

Target Market(s)

The concert is attended by several hundred family & friends

Industry/Entity Type

Dance Studio

Requirements
Must have
• Must have
• Let's Dance
• BRK logo (file supplied)
• 'The Maribel Crowe Dancers' (font is Mistral)
• Date of the concert: Saturday 14th November 2015
• Pellow Theatre, Saint Fenwick College Dalebrook
Nice to have
• We like clean design with no cluttered imagery.

```html
<!DOCTYPE html>
<html lang="en">
<head>
<meta charset="utf-8">
<title>Let's Dance – The Maribel Crowe Dancers</title>
<link href="https://fonts.googleapis.com/css2?family=Bebas+Neue&family=Kaushan+Script&display=swap" rel="stylesheet">
<style>
  :root {
    --ink: #111111;
    --white: #ffffff;
    --pink: #ff3fa4;
    --magenta: #d63cff;
    --violet: #7a4dff;
    --blue: #2fa8ff;
    --cyan: #2fe6e0;
    --green: #6fe86a;
    --yellow: #ffe94a;
    --orange: #ff9a3a;
    --red: #ff3b4e;
  }
  html, body {
    margin: 0;
    padding: 0;
    overflow: hidden;
    background: var(--white);
  }
  .poster {
    position: relative;
    width: 849px;
    height: 1200px;
    overflow: hidden;
    color: var(--ink);
  }
  .burst-backdrop {
    position: absolute;
    inset: 0;
    background:
      radial-gradient(ellipse 46% 40% at 50% 48%, var(--white) 0%, rgba(255,255,255,0.92) 35%, rgba(255,255,255,0) 100%),
      conic-gradient(from 0deg at 50% 48%,
        var(--yellow), var(--orange), var(--red), var(--pink), var(--magenta),
        var(--violet), var(--blue), var(--cyan), var(--green), var(--yellow));
  }
  .content {
    position: absolute;
    inset: 0;
    text-align: center;
  }
  .brand-mark {
    position: absolute;
    top: 40px;
    left: 0;
    right: 0;
    display: flex;
    justify-content: center;
    align-items: center;
    gap: 12px;
  }
  .brand-mark__dot {
    width: 26px;
    height: 26px;
    border-radius: 50%;
    background: var(--ink);
  }
  .brand-mark__name {
    font-family: "Bebas Neue", sans-serif;
    font-size: 56px;
    line-height: 1;
    letter-spacing: 4px;
  }
  .school-name {
    position: absolute;
    top: 97px;
    left: 0;
    right: 0;
    margin: 0;
    font-family: "Kaushan Script", cursive;
    font-weight: 400;
    font-size: 44px;
    line-height: 1.2;
  }
  .presents {
    position: absolute;
    top: 170px;
    left: 0;
    right: 0;
    margin: 0;
    font-family: "Bebas Neue", sans-serif;
    font-size: 30px;
    letter-spacing: 14px;
    padding-left: 14px;
  }
  .show-title {
    position: absolute;
    top: 330px;
    left: 0;
    right: 0;
    margin: 0;
    font-family: "Bebas Neue", sans-serif;
    font-weight: 400;
    font-size: 232px;
    line-height: 0.84;
    letter-spacing: 6px;
  }
  .show-title span { display: block; }
  .event-details {
    position: absolute;
    top: 960px;
    left: 0;
    right: 0;
    font-family: "Bebas Neue", sans-serif;
    font-size: 34px;
    line-height: 1.2;
    letter-spacing: 3px;
  }
  .event-details p { margin: 0; }
</style>
</head>
<body>
  <main class="poster">
    <div class="burst-backdrop" role="img" aria-label="Bright rainbow sunburst of rays radiating from a white centre"></div>
    <div class="content">
      <div class="brand-mark">
        <span class="brand-mark__dot"></span>
        <span class="brand-mark__name">BRK</span>
      </div>
      <h2 class="school-name">The Maribel Crowe Dancers</h2>
      <p class="presents">PRESENTS</p>
      <h1 class="show-title"><span>LET'S</span><span>DANCE</span></h1>
      <div class="event-details">
        <p class="event-date">Saturday 14th November 2015</p>
        <p class="event-venue">Pellow Theatre, Saint Fenwick College Dalebrook</p>
      </div>
    </div>
  </main>
</body>
</html>
```